Service business needs Business Card Design

Looking to create a new business card design that is both professional and unique the can highlight the many services we offer throughout the seasons. Our tagline is "The Cobalt Advantage"
Licensed & Insured: HC731462 has to be small and on the back side of the card.
On the Front:
FirstName LastName
Title
We offer the following services:
Deck Repair and Maintenance
Deck Cleaning and Staining/Painting
Power Washing/House Washing
Landscape Lighting Installation
Christmas Lighting Installation

```html
<!DOCTYPE html>
<html lang="en">
<head>
<meta charset="utf-8">
<title>Clearline Services — Business Card</title>
<link href="https://fonts.googleapis.com/css2?family=Lato:wght@400;700&family=Saira+Semi+Condensed:wght@700&display=swap" rel="stylesheet">
<style>
  :root {
    --backdrop: #1c1c1e;
    --card-white: #ffffff;
    --navy: #0d4a86;
    --deep-blue: #004b8c;
    --sky: #2ab4e8;
    --ink: #3a3a3a;
    --soft-wash: #e6eef6;
    --soft-glow: #f1f9fe;
    --pale-text: #cfe0f0;
  }
  * { box-sizing: border-box; margin: 0; padding: 0; }
  html, body { width: 1200px; height: 1200px; overflow: hidden; }
  body { background: var(--backdrop); position: relative; font-family: "Lato", sans-serif; }

  .card {
    position: absolute; left: 281px; width: 638px; height: 366px;
    border-radius: 24px; overflow: hidden;
  }
  .card--front { top: 195px; background: var(--card-white); }
  .card--back { top: 639px; background: var(--deep-blue); }

  /* front */
  .front-wash {
    position: absolute; left: 0; top: 0; width: 360px; height: 366px;
    background: linear-gradient(120deg, var(--soft-glow) 0%, var(--soft-wash) 100%);
    border-radius: 0 180px 180px 0;
  }
  .service-list { position: absolute; left: 34px; top: 44px; list-style: none; }
  .service {
    display: flex; align-items: center; gap: 14px;
    height: 44px; margin-bottom: 15.5px;
  }
  .service-tick { width: 30px; height: 30px; flex: none; }
  .service-name {
    color: var(--navy); font-size: 18px; line-height: 21px;
    letter-spacing: 0.4px; text-transform: uppercase;
  }

  .contact { position: absolute; right: 37px; top: 0; text-align: right; }
  .brand {
    position: absolute; right: 0; top: 98px; white-space: nowrap;
    display: flex; align-items: center; gap: 8px;
    color: var(--navy); font-weight: 700; font-size: 20px; letter-spacing: 1.5px;
  }
  .brand-mark { width: 14px; height: 14px; background: var(--navy); }
  .person-name {
    position: absolute; right: 0; top: 166px; white-space: nowrap;
    font-family: "Saira Semi Condensed", sans-serif; font-weight: 700;
    font-size: 30px; line-height: 30px; color: var(--navy);
  }
  .person-title {
    position: absolute; right: 0; top: 197px; white-space: nowrap;
    color: var(--sky); font-size: 17px;
  }
  .detail {
    position: absolute; right: 0; white-space: nowrap;
    display: flex; align-items: center; gap: 7px; color: var(--ink);
  }
  .detail svg { width: 11px; height: 11px; }
  .detail--phone { top: 233px; font-size: 16px; font-weight: 700; }
  .detail--email { top: 258px; font-size: 13px; }
  .detail--web { top: 278px; font-size: 13px; }

  /* back */
  .back-glow {
    position: absolute; right: 0; top: 0; width: 380px; height: 366px;
  }
  .back-brand {
    position: absolute; left: 88px; top: 200px; white-space: nowrap;
    display: flex; align-items: center; gap: 7px;
    color: var(--card-white); font-weight: 700; font-size: 17px; letter-spacing: 1.3px;
  }
  .back-brand .brand-mark { background: var(--card-white); width: 12px; height: 12px; }
  .tagline {
    position: absolute; left: 39px; top: 243px;
    font-family: "Saira Semi Condensed", sans-serif; font-weight: 700;
    color: var(--card-white); text-transform: uppercase; line-height: 1;
  }
  .tagline-top { display: block; font-size: 38px; letter-spacing: 1px; }
  .tagline-bottom { display: block; font-size: 46px; letter-spacing: 1px; margin-top: -2px; }
  .license {
    position: absolute; left: 40px; top: 340px; white-space: nowrap;
    font-size: 10px; color: var(--pale-text); letter-spacing: 0.3px;
  }
</style>
</head>
<body>

<section class="card card--front" aria-label="Card front">
  <div class="front-wash"></div>
  <ul class="service-list">
    <li class="service">
      <svg class="service-tick" viewBox="0 0 30 30"><circle cx="15" cy="15" r="15" fill="#2ab4e8"/><path d="M8.5 15.5l4.5 4.5 8.5-9" fill="none" stroke="#fff" stroke-width="3.4" stroke-linecap="round" stroke-linejoin="round"/></svg>
      <span class="service-name">Deck Repair &amp;<br>Maintenance</span>
    </li>
    <li class="service">
      <svg class="service-tick" viewBox="0 0 30 30"><circle cx="15" cy="15" r="15" fill="#2ab4e8"/><path d="M8.5 15.5l4.5 4.5 8.5-9" fill="none" stroke="#fff" stroke-width="3.4" stroke-linecap="round" stroke-linejoin="round"/></svg>
      <span class="service-name">Deck Cleaning &amp;<br>Staining/Painting</span>
    </li>
    <li class="service">
      <svg class="service-tick" viewBox="0 0 30 30"><circle cx="15" cy="15" r="15" fill="#2ab4e8"/><path d="M8.5 15.5l4.5 4.5 8.5-9" fill="none" stroke="#fff" stroke-width="3.4" stroke-linecap="round" stroke-linejoin="round"/></svg>
      <span class="service-name">Power Washing/<br>House Washing</span>
    </li>
    <li class="service">
      <svg class="service-tick" viewBox="0 0 30 30"><circle cx="15" cy="15" r="15" fill="#2ab4e8"/><path d="M8.5 15.5l4.5 4.5 8.5-9" fill="none" stroke="#fff" stroke-width="3.4" stroke-linecap="round" stroke-linejoin="round"/></svg>
      <span class="service-name">Landscape Lighting<br>Installation</span>
    </li>
    <li class="service">
      <svg class="service-tick" viewBox="0 0 30 30"><circle cx="15" cy="15" r="15" fill="#2ab4e8"/><path d="M8.5 15.5l4.5 4.5 8.5-9" fill="none" stroke="#fff" stroke-width="3.4" stroke-linecap="round" stroke-linejoin="round"/></svg>
      <span class="service-name">Christmas Lighting<br>Installation</span>
    </li>
  </ul>

  <div class="contact">
    <div class="brand"><span class="brand-mark"></span>CLEARLINE SERVICES</div>
    <div class="person-name">DANIEL REYES</div>
    <div class="person-title">Founder &amp; CEO</div>
    <div class="detail detail--phone">215.555.0142
      <svg viewBox="0 0 12 12"><path d="M2.5 1l2 2.4-1.1 1.3c.7 1.5 1.8 2.6 3.3 3.3l1.3-1.1L10.5 9l-1.4 1.8C5 10.5 1.4 7 1 2.6z" fill="#2ab4e8"/></svg>
    </div>
    <div class="detail detail--email">info@clearlineservicesco.com
      <svg viewBox="0 0 12 12"><rect x="0.5" y="2" width="11" height="8" fill="#2ab4e8"/><path d="M1 2.5l5 4 5-4" fill="none" stroke="#fff" stroke-width="1"/></svg>
    </div>
    <div class="detail detail--web">clearlineservicesco.com
      <svg viewBox="0 0 12 12"><circle cx="6" cy="6" r="5.3" fill="none" stroke="#2ab4e8" stroke-width="1.4"/><ellipse cx="6" cy="6" rx="2" ry="5.3" fill="none" stroke="#2ab4e8" stroke-width="1"/></svg>
    </div>
  </div>
</section>

<section class="card card--back" aria-label="Card back">
  <svg class="back-glow" viewBox="0 0 380 366" role="img" aria-label="Decorative burst of light rays radiating from the top-right corner">
    <defs>
      <radialGradient id="glow" cx="1" cy="0" r="1.1">
        <stop offset="0" stop-color="#ffffff" stop-opacity="0.85"/>
        <stop offset="0.55" stop-color="#ffffff" stop-opacity="0.25"/>
        <stop offset="1" stop-color="#ffffff" stop-opacity="0"/>
      </radialGradient>
    </defs>
    <polygon points="100,0 380,0 380,366 40,366 20,230 10,120" fill="url(#glow)"/>
  </svg>
  <div class="back-brand"><span class="brand-mark"></span>CLEARLINE SERVICES</div>
  <h1 class="tagline">
    <span class="tagline-top">The Cobalt</span>
    <span class="tagline-bottom">Advantage</span>
  </h1>
  <div class="license">Licensed &amp; Insured: HC731462</div>
</section>

</body>
</html>
```